New Advertising Company Business Card

A two sided business card. One side with logo only and the other side with my information and maybe my logo again. Looking for something unique and creative, but not too busy. Info would include my name(Marcus Feldon), President, phone number, address, email address, and website. LOGO IS THE BLUE AND WHITE ONE.

Target Market(s)

CEO/VP Level Audience

Industry/Entity Type

Business

Contact Information for Business Card

In Description.

```html
<!DOCTYPE html>
<html lang="en">
<head>
<meta charset="utf-8">
<title>Lumen Advertising – Business Card</title>
<link href="https://fonts.googleapis.com/css2?family=Open+Sans:wght@400;600;700&display=swap" rel="stylesheet">
<style>
  :root {
    --page-bg: #1c1c1e;
    --card-dark: #101011;
    --brand-blue: #1f7ac4;
    --text-light: #f2f2f2;
    --text-muted: #cfcfcf;
  }
  * { margin: 0; padding: 0; box-sizing: border-box; }
  html, body { width: 1200px; height: 900px; overflow: hidden; }
  body {
    background: var(--page-bg);
    font-family: "Open Sans", sans-serif;
    display: flex;
    align-items: center;
    justify-content: center;
    gap: 60px;
  }
  .card {
    width: 525px;
    height: 300px;
    position: relative;
    border-radius: 4px;
    overflow: hidden;
    box-shadow: 0 14px 30px rgba(0,0,0,.45);
  }
  /* Information side */
  .card-front { background: var(--card-dark); color: var(--text-light); }
  .front-brand {
    position: absolute;
    top: 48px;
    right: 44px;
    display: flex;
    align-items: center;
    gap: 10px;
  }
  .brand-dot {
    width: 16px; height: 16px;
    border-radius: 50%;
    background: var(--brand-blue);
  }
  .brand-name {
    font-weight: 700;
    font-size: 24px;
    letter-spacing: 3px;
    color: var(--text-light);
  }
  .person {
    position: absolute;
    top: 130px;
    left: 40px;
    text-align: right;
    width: 200px;
  }
  .person-name { font-weight: 600; font-size: 20px; letter-spacing: .5px; text-transform: uppercase; }
  .person-role { font-size: 12px; color: var(--brand-blue); text-transform: uppercase; margin-top: 2px; }
  .divider {
    position: absolute;
    top: 124px;
    left: 262px;
    width: 1px;
    height: 64px;
    background: linear-gradient(to bottom, transparent, #d8d8d8, transparent);
  }
  .contact-list {
    position: absolute;
    top: 122px;
    left: 282px;
    list-style: none;
    font-size: 13.5px;
  }
  .contact-list li { display: flex; align-items: center; gap: 9px; height: 23px; }
  .contact-icon {
    width: 17px; height: 17px;
    border-radius: 50%;
    background: var(--brand-blue);
    display: flex; align-items: center; justify-content: center;
  }
  .address {
    position: absolute;
    left: 40px;
    bottom: 42px;
    font-size: 13.5px;
    color: var(--text-light);
  }
  .accent-band {
    position: absolute;
    left: 0; right: 0; bottom: 0;
    height: 14px;
    background: var(--brand-blue);
  }
  /* Logo side */
  .card-back {
    background: linear-gradient(160deg, #1872bd, #2b86cc);
    display: flex; align-items: center; justify-content: center;
    gap: 12px;
  }
  .card-back .brand-name { font-size: 30px; letter-spacing: 4px; color: #ffffff; }
  .card-back .brand-dot { background: #ffffff; width: 20px; height: 20px; }
</style>
</head>
<body>
  <section class="card card-front" aria-label="Business card information side">
    <div class="front-brand">
      <span class="brand-dot"></span>
      <span class="brand-name">LUMEN ADVERTISING</span>
    </div>

    <div class="person">
      <p class="person-name">Owen Carter</p>
      <p class="person-role">Managing Director</p>
    </div>

    <div class="divider"></div>

    <ul class="contact-list">
      <li>
        <span class="contact-icon">
          <svg width="10" height="10" viewBox="0 0 24 24" fill="#fff"><path d="M6.6 10.8a15.1 15.1 0 0 0 6.6 6.6l2.2-2.2a1 1 0 0 1 1-.25 11.4 11.4 0 0 0 3.6.57 1 1 0 0 1 1 1V20a1 1 0 0 1-1 1A17 17 0 0 1 3 4a1 1 0 0 1 1-1h3.5a1 1 0 0 1 1 1c0 1.25.2 2.45.57 3.57a1 1 0 0 1-.25 1z"/></svg>
        </span>
        27 10 555 0148
      </li>
      <li>
        <span class="contact-icon">
          <svg width="10" height="10" viewBox="0 0 24 24" fill="none" stroke="#fff" stroke-width="2.4"><rect x="3" y="5" width="18" height="14"/><path d="M3 5l9 8 9-8"/></svg>
        </span>
        owen@lumenad.com
      </li>
      <li>
        <span class="contact-icon">
          <svg width="10" height="10" viewBox="0 0 24 24" fill="none" stroke="#fff" stroke-width="2.2"><circle cx="12" cy="12" r="9"/><path d="M3 12h18M12 3c3 3 3 15 0 18M12 3c-3 3-3 15 0 18"/></svg>
        </span>
        www.lumenad.com
      </li>
    </ul>

    <p class="address">42 Meridian Park Drive, Suite 210, Fairview, NJ</p>
    <div class="accent-band"></div>
  </section>

  <section class="card card-back" aria-label="Business card logo side">
    <span class="brand-dot"></span>
    <span class="brand-name">LUMEN ADVERTISING</span>
  </section>
</body>
</html>
```